Design a Brochure for curtain and fabric company

I require a brochure designed for my curtain and fabric company.

I am looking for something unique that will look classy and enticing. I have the wording in the document attached. I have quality pictures here: https://www.filmaveroq.net/sh/4qm2tbx9wlrpfhk/aRtyk3cLWQ

Logos Attached. I have also attached my business card so you can see my branding style.

Fonts: (NOTE ANY OTHER FONT WILL BE FINE TOO IF YOU THINK IT"S BETTER)
Trajan Pro – regular
Century Gothic – regular

Peach colour: #f8b882

Please let me know if you require anything else or more info.

I have attached a mock up with specs and also business card so you get a good idea of what my style is.

Requirements:

Has to look sophisticated and classy.

```html
<!DOCTYPE html>
<html lang="en">
<head>
<meta charset="utf-8">
<title>Drapé Maison – Brochure Spreads</title>
<link href="https://fonts.googleapis.com/css2?family=Cinzel:wght@400&family=Questrial&display=swap" rel="stylesheet">
<style>
  :root{
    --peach:#f8b882;
    --charcoal:#3a3a3c;
    --ink:#2b2b2b;
    --paper:#ffffff;
    --stage:#e9e6e2;
    --muted:#d8d4cf;
    --serif:'Cinzel', serif;
    --sans:'Questrial', sans-serif;
  }
  *{box-sizing:border-box;margin:0;padding:0}
  html,body{width:1200px;height:800px;overflow:hidden}
  body{background:var(--stage);position:relative;font-family:var(--sans);color:var(--ink)}
  .spread{position:absolute;width:450px;height:228px;background:var(--paper);overflow:hidden;box-shadow:0 2px 8px rgba(0,0,0,.18)}
  .spread--cover{left:150px;top:28px}
  .spread--intro{left:620px;top:28px}
  .spread--range{left:150px;top:282px}
  .spread--ready{left:620px;top:282px}
  .spread--order{left:150px;top:536px}
  .photo{position:absolute}
  .block{position:absolute}
  .dark{background:var(--charcoal);color:#eee}
  .peach{background:var(--peach);color:#fff}
  .title{font-family:var(--serif);font-weight:400;letter-spacing:.5px}
  .body-copy{font-size:5.6px;line-height:1.45;color:#e6e6e6}
  .body-copy p{margin-bottom:4px}

  /* cover */
  .cover-fabric{left:0;top:0;width:225px;height:228px;background:linear-gradient(135deg,#f2f1ef 0%,#cfccc8 45%,#f4f3f1 60%,#bdb9b4 100%)}
  .cover-room{left:225px;top:0;width:225px;height:228px;background:linear-gradient(90deg,#2d2320 0%,#6b5a50 25%,#e8e1d6 40%,#3a2d28 55%,#d9d2c6 70%,#4a3a33 85%,#e4ddd2 100%)}
  .cover-band{left:0;top:92px;width:450px;height:48px;background:rgba(255,255,255,.78)}
  .cover-contact{left:0;top:98px;width:215px;text-align:right;font-size:6.4px;line-height:1.45;color:#444}
  .cover-contact .phone{font-size:7px;color:#222}
  .brand{left:240px;top:100px;width:200px;text-align:center}
  .brand-name{font-family:var(--serif);font-size:21px;color:#5a5a5a;letter-spacing:1.5px}
  .brand-tag{font-size:5px;color:#666;letter-spacing:.6px;margin-top:1px}

  /* intro */
  .intro-window{left:0;top:0;width:225px;height:228px;background:linear-gradient(90deg,#2a2522 0%,#7d7068 18%,#e8efe9 32%,#8fae86 50%,#e6ece6 66%,#6e625b 82%,#2a2522 100%)}
  .intro-label{left:0;top:170px;width:88px;height:58px;display:flex;align-items:center;justify-content:center;font-size:8px;text-align:center}
  .intro-caption{left:92px;top:176px;width:120px;font-size:5.4px;line-height:1.45;color:#eee}
  .intro-grommet{left:225px;top:0;width:120px;height:228px;background:radial-gradient(circle at 45% 32%,#fff 0 13px,#d9d9d9 14px 18px,transparent 19px),linear-gradient(160deg,#7c1418 0%,#b42228 35%,#2a1a1a 60%,#a01c22 100%)}
  .intro-col{left:345px;top:0;width:105px;height:228px}
  .intro-head{left:345px;top:0;width:105px;height:64px;padding:8px;font-size:6.6px;line-height:1.3}
  .intro-body{left:352px;top:72px;width:92px}

  /* range */
  .range-window{left:0;top:0;width:225px;height:228px;background:linear-gradient(90deg,#2b2522 0%,#6b5f57 20%,#eaf0ea 34%,#9ab692 50%,#eef2ee 64%,#6b5f57 80%,#2b2522 100%)}
  .range-label{left:0;top:128px;width:88px;height:46px;display:flex;flex-direction:column;align-items:center;justify-content:center;font-size:7.5px;text-align:center;line-height:1.3}
  .range-fabric{left:225px;top:0;width:120px;height:228px;background:linear-gradient(135deg,#eef1f0 0%,#2f9aa6 30%,#f0f2f1 50%,#2a8f9b 70%,#e8ecea 100%)}
  .range-col{left:345px;top:0;width:105px;height:228px}
  .range-head{left:345px;top:26px;width:105px;height:60px;padding:7px 8px;font-size:6.2px;line-height:1.3}
  .range-body{left:352px;top:96px;width:92px}

  /* ready */
  .ready-fabric{left:0;top:0;width:340px;height:228px;background:linear-gradient(120deg,#f1f3f2 0%,#3aa3ae 22%,#eef1f0 40%,#2d939f 58%,#f2f4f3 76%,#3aa3ae 100%)}
  .ready-rod{left:0;top:56px;width:220px;height:14px;background:linear-gradient(#222,#444 50%,#1a1a1a)}
  .ready-title{left:26px;top:96px;font-size:17px;color:#fff;text-shadow:0 1px 2px rgba(0,0,0,.35)}
  .ready-col{left:340px;top:0;width:110px;height:228px}
  .ready-body{left:348px;top:52px;width:94px}

  /* order */
  .order-room{left:0;top:0;width:450px;height:228px;background:linear-gradient(90deg,#e9e3d8 0%,#5e4b40 12%,#e8e1d5 22%,#2e2623 34%,#e6ded2 46%,#b9a898 60%,#efe9df 78%,#8a7868 100%)}
  .order-panel{left:225px;top:72px;width:225px;height:156px}
  .order-col{left:232px;top:82px;width:80px}
  .order-col .title,.design-col .title{font-size:8.5px;color:#fff;margin-bottom:5px}
  .design-col{left:318px;top:82px;width:126px}
  .design-col ol{padding-left:8px}
  .design-col li{margin-bottom:2px}
  .design-col ul{list-style:none;padding-left:3px}
</style>
</head>
<body>

<!-- Cover spread -->
<section class="spread spread--cover">
  <div class="photo cover-fabric" role="img" aria-label="Close-up photo of soft white curtain fabric folds"></div>
  <div class="photo cover-room" role="img" aria-label="Photo of patterned black and cream drapes hanging in a living room"></div>
  <div class="block cover-band"></div>
  <div class="block cover-contact">
    <p>www.drapemaison.com.au</p>
    <p>sales@drapemaison.com.au</p>
    <p style="margin-top:3px">Australia</p>
    <p class="phone">1800 000 000</p>
  </div>
  <div class="block brand">
    <div class="brand-name">DRAPÉ MAISON</div>
    <div class="brand-tag">Ready window drapes for stylish living</div>
  </div>
</section>

<!-- Intro spread -->
<section class="spread spread--intro">
  <div class="photo intro-window" role="img" aria-label="Photo of damask drapes framing a window onto a garden"></div>
  <div class="block intro-label peach title">Design-A-Drape</div>
  <p class="block intro-caption">Design your own drapes from our curated fabric collection</p>
  <div class="photo intro-grommet" role="img" aria-label="Close-up photo of a red and black drape with a silver eyelet on a curtain rod"></div>
  <div class="block intro-col dark"></div>
  <h2 class="block intro-head peach title">Curtains are the key to a beautifully designed room.</h2>
  <div class="block intro-body body-copy">
    <p>Drapé Maison is the premier brand and designer. We have been passionate about designing and making the finest ready-to-hang curtains in Australia.</p>
    <p>Not all window sizes are the same, so our Design-A-Drape range lets drapes be customised and made-to-order.</p>
    <p>Our ready-to-hang range is sold through boutique window furnishing retailers, interior designers and architects.</p>
  </div>
</section>

<!-- Range spread -->
<section class="spread spread--range">
  <div class="photo range-window" role="img" aria-label="Photo of black and cream patterned drapes beside a sunny window"></div>
  <div class="block range-label peach title"><span>Maren Black</span><span>(Ruche)</span></div>
  <div class="photo range-fabric" role="img" aria-label="Photo of a teal and white patterned drape held by a rope tie-back"></div>
  <div class="block range-col dark"></div>
  <h2 class="block range-head peach title">At Drapé Maison we are here to complete the look of your room.</h2>
  <div class="block range-body body-copy">
    <p>Homeowners today have a wide range of options when it comes to window dressing, but nothing adds elegance like designer drapes.</p>
    <p>Our drapes are sought after for their versatility and ability to effortlessly add style to any room.</p>
    <p>They add a softening touch over the hard edges of window frames, either on their own or over blinds.</p>
  </div>
</section>

<!-- Ready-to-hang spread -->
<section class="spread spread--ready">
  <div class="photo ready-fabric" role="img" aria-label="Close-up photo of teal patterned drape with eyelets on a black rod"></div>
  <div class="block ready-rod"></div>
  <h2 class="block ready-title title">Ready-to-hang</h2>
  <div class="block ready-col dark"></div>
  <div class="block ready-body body-copy">
    <p>Need drapes in a hurry? Buy pre-made ready-to-hang drapery panels from our select window furnishing retailers for designer trends for your home in a flash.</p>
  </div>
</section>

<!-- Order spread -->
<section class="spread spread--order">
  <div class="photo order-room" role="img" aria-label="Photo of a living room with striped and patterned drapes, a red lamp and a side table"></div>
  <div class="block order-panel dark"></div>
  <div class="block order-col body-copy">
    <h2 class="title">Order today!</h2>
    <p>All Drapé Maison products come with a 5 year warranty.</p>
  </div>
  <div class="block design-col body-copy">
    <h2 class="title">Design-A-Drape</h2>
    <ol>
      <li>Fabrics – choose from a range of versatile fabrics for the perfect look</li>
      <li>Style – choose from our many styles to get creative and design something uniquely yours:
        <ul><li>- Select a header style</li><li>- Add banding and elements</li></ul>
      </li>
      <li>Lining – select from unlined, blockout, thermal or triple weave</li>
      <li>Your designer quality drapes will be beautifully crafted</li>
    </ol>
  </div>
</section>

</body>
</html>
```